Medical Company in need of Modern business card design for new Wound Care clinic.

Modern business card design for our Woundcare company. Logo and description of services can be found on our website; https://www.tovrel-woundcare.com/

```html
<!DOCTYPE html>
<html lang="en">
<head>
<meta charset="UTF-8">
<title>Tovrel Woundcare – Business Card</title>
<link href="https://fonts.googleapis.com/css2?family=Raleway:wght@400;500;700&display=swap" rel="stylesheet">
<style>
  :root {
    --page-bg: #111111;
    --card-light: #f8f8f8;
    --front-start: #969695;
    --front-mid: #7a7a7a;
    --front-end: #474747;
    --gold: #d2a24c;
    --gold-soft: #f0c27a;
    --ink: #111111;
    --ink-soft: #2a2a2a;
  }
  * { margin: 0; padding: 0; box-sizing: border-box; }
  html, body {
    width: 1200px; height: 1000px; overflow: hidden;
    background: var(--page-bg);
    font-family: "Raleway", Arial, sans-serif;
  }
  .canvas { position: relative; width: 1200px; height: 1000px; }
  .card {
    position: absolute; left: 286px; width: 613px; height: 352px;
    border-radius: 36px; overflow: hidden;
  }
  .card-front {
    top: 102px;
    background: linear-gradient(90deg, var(--front-start) 0%, var(--front-mid) 45%, var(--front-end) 100%);
  }
  .front-wordmark {
    position: absolute; right: 56px; top: 346px;
    transform: translateY(-246px);
    display: flex; align-items: center; gap: 8px;
    color: var(--gold); font-size: 13px; font-weight: 500; letter-spacing: 2.5px;
  }
  .mark-dot { width: 14px; height: 14px; border-radius: 50%; background: var(--gold); }
  .card-back { top: 512px; background: var(--card-light); }
  .brand {
    position: absolute; left: 0; right: 0; top: 50px;
    display: flex; flex-direction: column; align-items: center;
  }
  .brand .mark-dot { width: 30px; height: 30px; margin-bottom: 16px; }
  .brand-name {
    color: var(--ink); font-size: 16px; font-weight: 500; letter-spacing: 3.2px;
    margin-left: 4px;
  }
  .holder {
    position: absolute; right: 324px; top: 183px; text-align: right;
  }
  .holder-name { font-size: 17px; font-weight: 700; color: var(--ink); line-height: 22px; }
  .holder-title { font-size: 15px; color: var(--ink-soft); line-height: 20px; }
  .divider {
    position: absolute; left: 308px; top: 181px; width: 2px; height: 52px;
    background: var(--gold-soft);
  }
  .contacts {
    position: absolute; left: 330px; top: 178px; list-style: none;
  }
  .contacts li {
    display: flex; align-items: center; gap: 9px;
    font-size: 13px; color: var(--ink-soft); line-height: 16.5px;
  }
  .contacts svg { width: 12px; height: 12px; fill: var(--gold-soft); }
  .address {
    position: absolute; left: 0; right: 0; top: 316px;
    padding-right: 36px; text-align: center; font-size: 13px; color: var(--ink-soft);
  }
</style>
</head>
<body>
<main class="canvas">
  <section class="card card-front" role="img" aria-label="Grey gradient card face with a repeating faint brand pattern">
    <div class="front-wordmark" style="transform:none; top:248px;">
      <span class="mark-dot"></span><span>TOVREL WOUNDCARE</span>
    </div>
  </section>

  <section class="card card-back">
    <div class="brand">
      <span class="mark-dot"></span>
      <span class="brand-name">TOVREL WOUNDCARE</span>
    </div>

    <div class="holder">
      <p class="holder-name">Name Surname</p>
      <p class="holder-title">Title</p>
    </div>
    <span class="divider"></span>

    <ul class="contacts">
      <li>
        <svg viewBox="0 0 24 24" aria-hidden="true"><path d="M6.6 10.8a15.1 15.1 0 0 0 6.6 6.6l2.2-2.2a1 1 0 0 1 1-.25 11.4 11.4 0 0 0 3.6.57 1 1 0 0 1 1 1V20a1 1 0 0 1-1 1A17 17 0 0 1 3 4a1 1 0 0 1 1-1h3.5a1 1 0 0 1 1 1c0 1.25.2 2.45.57 3.57a1 1 0 0 1-.25 1z"/></svg>
        <span>972-555-0148</span>
      </li>
      <li>
        <svg viewBox="0 0 24 24" aria-hidden="true"><path d="M2 5h20v14H2z M3 6l9 7 9-7" stroke="#f8f8f8" stroke-width="1.6"/></svg>
        <span>name@tovrel-woundcare.com</span>
      </li>
      <li>
        <svg viewBox="0 0 24 24" aria-hidden="true"><circle cx="12" cy="12" r="10"/><path d="M2 12h20M12 2c3 3 3 17 0 20M12 2c-3 3-3 17 0 20" stroke="#f8f8f8" stroke-width="1.4" fill="none"/></svg>
        <span>tovrel-woundcare.com</span>
      </li>
    </ul>

    <p class="address">2180 Alder Ridge Rd Ste 200 PMB 104827 Dallas, TX 75231</p>
  </section>
</main>
</body>
</html>
```